Business Card Kelda Law llc examples and ideas are attached.

in addition to the logo we need a desription what we do: "Reprsenting students with disabilites obtain services to progress in the public school system."

If you can squeeze it on the fron at the bottom great if not put it on the back

```html
<!DOCTYPE html>
<html lang="en">
<head>
<meta charset="utf-8">
<title>Kelda Law llc – Business Card</title>
<link rel="stylesheet" href="https://fonts.googleapis.com/css2?family=Alegreya:ital,wght@0,800;1,700;1,800&family=EB+Garamond:ital,wght@0,400;1,400&display=swap">
<style>
  :root {
    --navy: #00305f;
    --gold: #a08448;
    --ink: #111111;
    --paper: #ffffff;
  }
  * { margin: 0; padding: 0; box-sizing: border-box; }
  html, body {
    width: 1200px;
    height: 720px;
    overflow: hidden;
    background: var(--paper);
  }
  .card {
    position: relative;
    width: 1200px;
    height: 720px;
    background: var(--paper);
    color: var(--ink);
  }
  .brand-mark {
    position: absolute;
    left: 79px;
    top: 69px;
    width: 397px;
    height: 397px;
    background: var(--navy);
    display: flex;
    align-items: center;
    justify-content: center;
  }
  .brand-mark__name {
    font-family: "Alegreya", Georgia, serif;
    font-weight: 800;
    font-size: 58px;
    color: var(--gold);
    letter-spacing: 1px;
  }
  .divider {
    position: absolute;
    left: 530px;
    top: 61px;
    width: 4px;
    height: 531px;
    background: var(--ink);
  }
  .line {
    position: absolute;
    white-space: nowrap;
    line-height: 1;
  }
  .bold-italic {
    font-family: "Alegreya", Georgia, serif;
    font-style: italic;
    font-weight: 800;
  }
  .serif {
    font-family: "EB Garamond", Georgia, serif;
    font-weight: 400;
  }
  .firm-name    { left: 586px; top: 114px; font-size: 54px; }
  .person-name  { left: 644px; top: 204px; font-size: 42px; }
  .person-title { left: 644px; top: 248px; font-size: 41px; }
  .street       { left: 644px; top: 326px; font-size: 35px; }
  .street sup   { font-size: 18px; vertical-align: 14px; }
  .city         { left: 644px; top: 372px; font-size: 41px; }
  .hours        { left: 644px; top: 416px; font-size: 37px; font-style: italic; }
  .phone        { left: 644px; top: 488px; font-size: 37px; }
  .email        { left: 652px; top: 528px; font-size: 41px; }
  .tagline {
    position: absolute;
    left: 0;
    width: 1200px;
    top: 642px;
    text-align: center;
    font-size: 22px;
    line-height: 1;
    padding-right: 10px;
  }
</style>
</head>
<body>
  <div class="card">
    <div class="brand-mark">
      <span class="brand-mark__name">Kelda Law</span>
    </div>

    <div class="divider"></div>

    <div class="line bold-italic firm-name">Kelda Law llc</div>
    <div class="line bold-italic person-name">Tobias R Vantreel</div>
    <div class="line serif person-title">Attorney at low</div>
    <div class="line bold-italic street">1457 SE 18<sup>th</sup>Ave</div>
    <div class="line serif city">Harbor Bend FL 33410</div>
    <div class="line serif hours">By appointment only</div>
    <div class="line bold-italic phone">+813 555 0142</div>
    <div class="line serif email">tobias.keldalaw@postmail.com</div>

    <p class="bold-italic tagline">Reprsenting students with disabilites obtain services to progress in the public school system.</p>
  </div>
</body>
</html>
```